Business card design for new, innovative company - BoldHarbor

We are a new company looking for a business card design that is fun, different and quirky. Must use corporate colour green - CMYK C:55, M:0, Y:100, K:0, and corporate colour grey - C:0, M:0, Y: 0, K:70.

We have developed the first real time data application, in which people are able to profile the data of their existing customers in order to pull out more good fit clients to direct their marketing activities at.

Industry/Entity Type

Marketing

Requirements
Must have
• Logo, name, title, telephone number, fax number, email, website, address

```html
<!DOCTYPE html>
<html lang="en">
<head>
<meta charset="utf-8">
<title>BoldHarbor Business Card</title>
<link rel="stylesheet" href="https://fonts.googleapis.com/css2?family=Open+Sans:wght@400;600;800&display=swap">
<style>
  :root {
    --brand-green: #7dc142;
    --brand-grey: #6d6e71;
    --card-white: #f1f1f1;
    --page-bg: #e4e4e2;
    --text-dark: #4a4a4c;
  }
  * { box-sizing: border-box; margin: 0; padding: 0; }
  html, body {
    width: 1200px;
    height: 900px;
    overflow: hidden;
    background: var(--page-bg);
    font-family: "Open Sans", Arial, sans-serif;
  }
  .canvas {
    position: relative;
    width: 1200px;
    height: 900px;
  }
  .card {
    position: absolute;
    width: 560px;
    height: 320px;
    box-shadow: 0 6px 18px rgba(0,0,0,0.18);
    overflow: hidden;
  }

  /* Front: green */
  .card-front {
    left: 110px;
    top: 90px;
    background: var(--brand-green);
    border-radius: 0 70px 0 70px;
    display: flex;
    flex-direction: column;
    align-items: center;
    justify-content: center;
  }
  .card-front .wordmark {
    color: #ffffff;
    font-weight: 800;
    font-size: 62px;
    letter-spacing: -2px;
    line-height: 1;
  }
  .card-front .website {
    margin-top: 34px;
    color: #ffffff;
    font-size: 15px;
    letter-spacing: 4px;
  }

  /* Back: white with details */
  .card-back {
    left: 530px;
    top: 480px;
    background: var(--card-white);
    border-radius: 70px 0 70px 0;
  }
  .symbol-area {
    position: absolute;
    left: 36px;
    top: 48px;
    width: 190px;
    height: 190px;
    border-radius: 36px;
    background: linear-gradient(135deg, #8a8b8e 0%, #9fcf6e 100%);
    opacity: 0.55;
  }
  .card-back .wordmark {
    position: absolute;
    right: 30px;
    top: 26px;
    color: var(--brand-green);
    font-weight: 800;
    font-size: 30px;
    letter-spacing: -1px;
    line-height: 1;
  }
  .person-name {
    position: absolute;
    right: 30px;
    top: 88px;
    color: var(--brand-green);
    font-weight: 600;
    font-size: 19px;
  }
  .contact-list {
    position: absolute;
    right: 28px;
    top: 128px;
    list-style: none;
    text-align: right;
  }
  .contact-list li {
    display: flex;
    justify-content: flex-end;
    align-items: center;
    gap: 8px;
    font-size: 12.5px;
    color: var(--text-dark);
    line-height: 21px;
  }
  .contact-list svg {
    width: 12px;
    height: 12px;
    fill: var(--brand-green);
    flex: none;
  }
  .divider {
    position: absolute;
    left: 250px;
    right: 28px;
    top: 246px;
    height: 2px;
    background: var(--brand-green);
  }
  .address {
    position: absolute;
    right: 28px;
    top: 256px;
    font-size: 13px;
    color: var(--text-dark);
    letter-spacing: 0.2px;
  }
</style>
</head>
<body>
<main class="canvas">

  <section class="card card-front" aria-label="Business card front">
    <div class="wordmark">BoldHarbor</div>
    <div class="website">www.boldharbor.com</div>
  </section>

  <section class="card card-back" aria-label="Business card back">
    <div class="symbol-area" role="img" aria-label="Large brand symbol area"></div>

    <div class="wordmark">BoldHarbor</div>
    <div class="person-name">Nadia Fenwick</div>

    <ul class="contact-list">
      <li>01632 960482
        <svg viewBox="0 0 24 24" aria-hidden="true"><path d="M6.6 10.8a15 15 0 0 0 6.6 6.6l2.2-2.2c.3-.3.7-.4 1-.2 1.1.4 2.3.6 3.6.6.6 0 1 .4 1 1V20c0 .6-.4 1-1 1A17 17 0 0 1 3 4c0-.6.4-1 1-1h3.5c.6 0 1 .4 1 1 0 1.3.2 2.5.6 3.6.1.3 0 .7-.2 1z"/></svg>
      </li>
      <li>01632 960482
        <svg viewBox="0 0 24 24" aria-hidden="true"><path d="M7 1h10a2 2 0 0 1 2 2v18a2 2 0 0 1-2 2H7a2 2 0 0 1-2-2V3a2 2 0 0 1 2-2zm0 3v14h10V4zm5 15.5a1 1 0 1 0 0 2 1 1 0 0 0 0-2z"/></svg>
      </li>
      <li>07700 900318
        <svg viewBox="0 0 24 24" aria-hidden="true"><path d="M6 2h9l3 3v4h1a3 3 0 0 1 3 3v7h-4v3H6v-3H2v-7a3 3 0 0 1 3-3h1zm2 2v5h8V6h-2V4zm0 12v4h8v-4z"/></svg>
      </li>
      <li>nadia.fenwick@corvalink.com
        <svg viewBox="0 0 24 24" aria-hidden="true"><path d="M2 5h20v14H2zm2 2v.5l8 5 8-5V7zm0 2.8V17h16V9.8l-8 5z"/></svg>
      </li>
      <li>www.boldharbor.com
        <svg viewBox="0 0 24 24" aria-hidden="true"><path d="M12 2a10 10 0 1 0 0 20 10 10 0 0 0 0-20zm6.9 9h-3a15 15 0 0 0-1.3-5.6A8 8 0 0 1 18.9 11zM12 4.1c.9 1.2 1.8 3.5 1.9 6.9h-3.8c.1-3.4 1-5.7 1.9-6.9zM9.4 5.4A15 15 0 0 0 8.1 11h-3a8 8 0 0 1 4.3-5.6zM5.1 13h3a15 15 0 0 0 1.3 5.6A8 8 0 0 1 5.1 13zm6.9 6.9c-.9-1.2-1.8-3.5-1.9-6.9h3.8c-.1 3.4-1 5.7-1.9 6.9zm2.6-1.3a15 15 0 0 0 1.3-5.6h3a8 8 0 0 1-4.3 5.6z"/></svg>
      </li>
    </ul>

    <div class="divider"></div>
    <div class="address">27a Millbrook Lane, Ely, Cambridgeshire, CB7 4QT</div>
  </section>

</main>
</body>
</html>
```